Cartwell - custom section required

Hi, I am preparing a new cartwell site (not yet active).

I want to add a section to a theme that will need to be built from liquid or HTLM or any way that works. This section will be part of the home page. This section will be for information purposes only. The section would help with explain about an outsole, my idea would to be exactly like a premium tyre shop advertises. see link. https://www.varnotyre.example/tyres/en-au/car/catalogue/product/glider-ktx
I have attached my mock up of how the section could look. I am looking for someone to code this section with the interactivity like the tyre site. For example: 1) see the sliders how the come across when you scroll down, with our different properties customised. 2) The image windows with the different angles being nicely interactive ti show largewr image when hovering over. 3) If we could do like they did when you press on the different part of the tyre (for our site it would be the outsole) how it lights up the areas and talks about the properties of that area. So our outsole different parts would light up with different explanations.

This section is a quirky idea but will only really work if it is interactive and very professional. It would be great if the content could be modified without too much difficulty. The section could be different to my mock up, creative ideas that contribute to the feel of this section are welcome.

The design must be compatible with Cartwell so I can just easily drop the code in to create the section.

Target Market(s)

Trendy people

Industry/Entity Type

Fashion

Coding

Coded - Design and coding required

Number of Pages Required

1 page

Requirements
Must have
• Must have responsiveness and animated as described.
Nice to have
• If the branding could be included it would be great.

```html
<!DOCTYPE html>
<html lang="en">
<head>
<meta charset="utf-8">
<title>Kin Crew – Performance Pro Outsole</title>
<link href="https://fonts.googleapis.com/css2?family=Poppins:wght@400;500;600;700;800&display=swap" rel="stylesheet">
<style>
  :root{
    --ink:#111;
    --text:#222;
    --muted:#555;
    --line:#e2e2e2;
    --soft:#eeeeee;
    --pill:#808080;
    --sole:#7d7f80;
    --accent:#e2ea00;
    --hot:#e8661a;
    --link:#4f7a7a;
    --dry:#0535e6;
    --wet:#ff7700;
    --club:#00f0f0;
    --bars:#0aa0f0;
    --music:#1a5fd0;
    --glamp:#8a00f0;
    --onpoint:#d4f000;
  }
  *{box-sizing:border-box;margin:0;padding:0}
  html,body{width:1200px;height:2198px;overflow:hidden;background:#fff}
  body{font-family:'Poppins',sans-serif;color:var(--text);position:relative}
  .abs{position:absolute}

  .top-strip{left:0;top:0;width:1200px;height:7px;background:linear-gradient(90deg,var(--ink) 0 591px,var(--accent) 591px)}
  .site-header{left:0;top:7px;width:1200px;height:96px;border-bottom:1px solid var(--line)}
  .brand{left:99px;top:26px;font-weight:800;font-size:40px;color:var(--ink);letter-spacing:1px;line-height:1}
  .account{left:819px;top:33px;font-size:17px;font-weight:600;color:var(--ink)}
  .account .login{color:var(--link)}
  .header-divider{left:984px;top:24px;width:1px;height:42px;background:var(--line)}
  .header-icons{left:1000px;top:36px;display:flex;gap:18px}
  .header-icons svg{width:18px;height:18px}
  .cart{position:relative}
  .cart-dot{position:absolute;right:-4px;top:-5px;width:9px;height:9px;border-radius:50%;background:#e00}

  .main-nav{left:0;top:103px;width:1200px;height:60px;border-bottom:1px solid var(--line)}
  .main-nav a{position:absolute;top:18px;transform:translateX(-50%);font-size:17px;color:var(--text);text-decoration:none;white-space:nowrap}
  .nav-sep{position:absolute;top:0;width:1px;height:60px;background:var(--line)}

  .badge-new{left:98px;top:188px;width:108px;height:48px;border-radius:24px;background:var(--pill);color:#fff;font-size:24px;display:flex;align-items:center;justify-content:center}
  .product-title{left:98px;top:265px;font-size:36px;font-weight:700;line-height:49px;color:var(--ink);letter-spacing:.5px}
  .fit-button{left:99px;top:390px;width:391px;height:75px;border-radius:12px;background:#262626;color:#fff;font-size:25px;display:flex;align-items:center;justify-content:center}

  .hero-visual{left:608px;top:230px;width:311px;height:451px;border-radius:150px 150px 120px 120px;background:radial-gradient(ellipse at 50% 45%,#8a8c8d,#6f7172 70%,#e9e9e9)}
  .thumb{left:978px;width:126px;height:144px;border-radius:14px;background:var(--soft);display:flex;align-items:center;justify-content:center}
  .thumb .shot{width:86px;border-radius:20px;background:linear-gradient(#8c8e8f,#6f7172)}

  .uses{left:98px;top:630px;display:flex}
  .use{width:88px;text-align:center}
  .use .glyph{display:block;margin:0 auto;width:40px;height:40px;border-radius:10px;background:linear-gradient(135deg,#d9d9d9,#b5b5b5)}
  .use .glyph.festival{background:linear-gradient(135deg,#ff9a4a,#4a7be0)}
  .use span{display:block;margin-top:22px;font-size:9px;font-weight:500;color:#333}

  .faint-backdrop{left:669px;top:849px;width:531px;height:942px;background:radial-gradient(ellipse at 60% 50%,rgba(200,200,200,.35),rgba(235,235,235,.15) 55%,rgba(255,255,255,0) 75%)}

  .section-title{left:101px;top:743px;font-size:24px;font-weight:600;color:var(--ink);letter-spacing:.5px}
  .tagline{left:103px;top:801px;font-size:26px;line-height:40px;color:var(--muted)}
  .description{left:103px;top:938px;width:530px;font-size:15px;line-height:27.4px;color:#333}

  .ratings{left:103px;top:1126px;width:522px}
  .rating{height:36.4px;position:relative}
  .rating .label{font-size:14px;font-weight:700;color:var(--ink);letter-spacing:.3px;line-height:18px}
  .rating .track{position:absolute;left:0;top:22px;width:522px;height:1px;background:#ddd}
  .rating .fill{position:absolute;left:0;top:19px;display:flex;gap:1px}
  .rating .fill i{display:block;width:50px;height:7px;background:var(--c)}

  .sole-explorer{left:146px;top:1453px;width:257px;height:236px;border-radius:110px 110px 0 0;background:linear-gradient(#868889,#6f7172)}
  .hotspot{width:42px;height:42px;border-radius:50%;background:var(--hot);display:flex;align-items:center;justify-content:center}
  .hotspot svg{width:22px;height:22px}
  .callout{left:438px;top:1463px;width:273px;height:104px;border:2px solid #d2d2d2;border-radius:14px;background:var(--soft);padding:12px 20px;font-size:17px;font-weight:700;line-height:27px;color:var(--ink)}

  .feature-heading{left:103px;top:1792px;font-size:21px;font-weight:700;line-height:40.4px;color:var(--ink);letter-spacing:.6px}

  .site-footer{left:0;top:2048px;width:1200px;height:150px;border-top:1px solid var(--line)}
  .footer-brand{left:103px;top:40px;font-size:22px;font-weight:800;color:var(--ink)}
  .footer-nav a{position:absolute;top:31px;font-size:15.5px;color:#333;text-decoration:none}
  .copyright{left:321px;top:88px;font-size:17px;color:var(--ink)}
</style>
</head>
<body>
  <div class="abs top-strip"></div>

  <header class="abs site-header">
    <div class="abs brand">KIN CREW</div>
    <div class="abs account"><span class="login">Login</span> or Register</div>
    <div class="abs header-divider"></div>
    <div class="abs header-icons">
      <svg viewBox="0 0 20 20"><circle cx="8" cy="8" r="6" fill="none" stroke="#111" stroke-width="2.6"/><path d="M12.5 12.5 18 18" stroke="#111" stroke-width="2.8" stroke-linecap="round"/></svg>
      <svg viewBox="0 0 20 20"><circle cx="10" cy="6" r="4.5" fill="#111"/><path d="M2 19c0-5 3.5-7 8-7s8 2 8 7z" fill="#111"/></svg>
      <span class="cart"><svg viewBox="0 0 20 20"><path d="M1 3h3l2.5 10h10L19 6H6" fill="none" stroke="#111" stroke-width="2.4" stroke-linejoin="round"/><circle cx="8" cy="17" r="1.8" fill="#111"/><circle cx="15" cy="17" r="1.8" fill="#111"/></svg><span class="cart-dot"></span></span>
    </div>
  </header>

  <nav class="abs main-nav">
    <a style="left:250px">Outsole's Catalogue</a>
    <span class="nav-sep" style="left:380px"></span>
    <a style="left:503px">Tech &amp; Knowledge</a>
    <span class="nav-sep" style="left:621px"></span>
    <a style="left:695px">Pulse™</a>
    <span class="nav-sep" style="left:768px"></span>
    <a style="left:826px">Tips</a>
    <span class="nav-sep" style="left:886px"></span>
    <a style="left:979px">Promotions</a>
  </nav>

  <div class="abs badge-new">NEW</div>
  <h1 class="abs product-title">KIN CREW'S PERFORMANCE<br>PRO OUTSOLE</h1>
  <div class="abs fit-button">FIT ON YOUR FOOT</div>

  <div class="abs hero-visual" role="img" aria-label="Pair of grey outsoles viewed from below"></div>
  <div class="abs thumb" style="top:188px" role="img" aria-label="Outsoles top view thumbnail"><div class="shot" style="height:110px;width:78px"></div></div>
  <div class="abs thumb" style="top:356px;background:#fff;box-shadow:0 2px 10px rgba(0,0,0,.08)" role="img" aria-label="Outsole heel angle thumbnail"><div class="shot" style="height:44px;width:100px;border-radius:10px"></div></div>
  <div class="abs thumb" style="top:523px" role="img" aria-label="Outsole side profile thumbnail"><div class="shot" style="height:40px;width:100px;border-radius:10px"></div></div>

  <div class="abs uses">
    <div class="use"><i class="glyph" role="img" aria-label="All weather icon"></i><span>ALL WEATHER</span></div>
    <div class="use"><i class="glyph" role="img" aria-label="Glamping tent icon"></i><span>GLAMPING</span></div>
    <div class="use"><i class="glyph" role="img" aria-label="Disco ball icon"></i><span>CLUBBING</span></div>
    <div class="use"><i class="glyph festival" role="img" aria-label="Festival crowd icon"></i><span>FESTIVALS</span></div>
  </div>

  <div class="abs faint-backdrop" role="img" aria-label="Faint decorative brand backdrop"></div>

  <h2 class="abs section-title">PERFORMANCE PRO OUTSOLE</h2>
  <p class="abs tagline">All weather is welcome.<br>Designed for rugged seasons<br>and unexpected kneesup</p>
  <p class="abs description">Kin Crew's Performance Pro is a high performance outsole that features an asymmetrical tread pattern and tread rigidity which ensures the best grip on wet surfaces, and outstanding handling performance on grassed areas. Dynamic Response technology optimizes dance precision for optimum grooves, from city clubs to wet field day</p>

  <div class="abs ratings">
    <div class="rating" style="--c:var(--dry)"><div class="label">DRY</div><div class="track"></div><div class="fill"><i></i><i></i><i></i><i></i><i></i><i></i></div></div>
    <div class="rating" style="--c:var(--wet)"><div class="label">WET</div><div class="track"></div><div class="fill"><i></i><i></i><i></i><i></i><i></i><i></i><i></i></div></div>
    <div class="rating" style="--c:var(--club)"><div class="label">CLUBBING</div><div class="track"></div><div class="fill"><i></i><i></i><i></i><i></i><i></i><i></i><i></i><i></i></div></div>
    <div class="rating" style="--c:var(--bars)"><div class="label">BARS</div><div class="track"></div><div class="fill"><i></i><i></i><i></i><i></i><i></i><i></i><i></i><i></i><i></i></div></div>
    <div class="rating" style="--c:var(--music)"><div class="label">MUSICFESTIVALS</div><div class="track"></div><div class="fill"><i></i><i></i><i></i><i></i><i></i><i></i><i></i><i></i></div></div>
    <div class="rating" style="--c:var(--glamp)"><div class="label">GLAMPING</div><div class="track"></div><div class="fill"><i></i><i></i><i></i><i></i><i></i><i></i><i></i><i></i><i></i></div></div>
    <div class="rating" style="--c:var(--onpoint)"><div class="label">ONPOINT</div><div class="track"></div><div class="fill"><i></i><i></i><i></i><i></i><i></i><i></i><i></i><i></i><i></i></div></div>
  </div>

  <div class="abs sole-explorer" role="img" aria-label="Interactive pair of outsoles with selectable zones"></div>
  <div class="abs hotspot" style="left:191px;top:1453px"><svg viewBox="0 0 22 22"><path d="M11 3v16M3 11h16" stroke="#111" stroke-width="4"/></svg></div>
  <div class="abs hotspot" style="left:379px;top:1558px"><svg viewBox="0 0 22 22"><path d="M11 3v16M3 11h16" stroke="#111" stroke-width="4"/></svg></div>
  <div class="abs hotspot" style="left:138px;top:1630px"><svg viewBox="0 0 22 22"><path d="M11 3v16M3 11h16" stroke="#111" stroke-width="4"/></svg></div>
  <div class="abs callout">Premium design for an appealing finish to your multipurpose boots.</div>

  <h3 class="abs feature-heading">LATERAL GROOVES FOR<br>RAPID WATER EXPULSION IN<br>WET CONDITIONS &amp; LOOKING<br>CHIC<br>REGARDLESS OF THE EVENT</h3>

  <footer class="abs site-footer">
    <div class="abs footer-brand">KIN CREW</div>
    <nav class="footer-nav">
      <a style="left:321px">Outsole's Catalogue</a>
      <a style="left:555px">Tech &amp; Knowledge</a>
      <a style="left:776px">Pulse™</a>
      <a style="left:902px">Tips</a>
      <a style="left:1011px">Promotions</a>
    </nav>
    <div class="abs copyright">© copyrights 2022 Kin Crew &nbsp;|&nbsp; All Rights Reserved</div>
  </footer>
</body>
</html>
```